Verpackungen Geschenkbox
Eine völlig unkomplizierte und tolle Zusammenarbeit. Und ein ganz tolles Ergebnis. Vielen Dank auch hier noch einmal : )
Zielgruppe
In unserem Studio können Kunden Keramik bemalen
Aufgabenstellung
Ich hätte gerne eine Vorlage für einen Aufkleber, den ich auf eine Verschenkbox machen kann. Diese Geschenkbox werde ich mit einer Rohkeramik füllen, zusätzlich alle Materialien die dafür benötigt werden, wie z.B. Glasuren, Pinsel etc. Diese Boxen sind fertig gerichtet, können direkt gekauft werden und die bemalte Keramik uns wieder zum Brennen gebracht werden. Der Aufkleber dazu soll zu unserem ganzen Stil passen und es soll unser Logo enthalten sein. Es soll zum Kaufen annimieren, aber nicht übertrieben sein. Eher klar auch in den Farben.
Der Aufkleber sollte max. 10 cm groß sein. Der Karton ist viereckig, unterschiedlich groß, so dass eine Tasse, Müslischale oder Teller reinpasst, mit ein paar kleine Fabdosen, Pinsel und anderes Materialien wie Schwamm oder Punktewerkzeug. Achtung, es ist keine Töpferei

```html
<!DOCTYPE html>
<html lang="de">
<head>
<meta charset="utf-8">
<title>Pinselhaus – Aufkleber Geschenkbox</title>
<link rel="stylesheet" href="https://fonts.googleapis.com/css2?family=EB+Garamond:wght@600;700&family=Noto+Sans:wght@400;700&display=swap">
<style>
  :root {
    --teal: #00798a;
    --ink: #137784;
    --paper: #ffffff;
    --stage: #eeeeee;
    --rule: #a3a3a3;
    --badge: #e2e4e4;
    --leaf: #cfe3e6;
    --leaf-soft: #eef5f6;
  }
  * { margin: 0; padding: 0; box-sizing: border-box; }
  html, body { width: 996px; height: 1200px; overflow: hidden; }
  body { position: relative; background: var(--teal); font-family: "Noto Sans", sans-serif; }

  .stage { position: absolute; left: 0; top: 0; width: 996px; height: 663px; background: var(--stage); }
  .showcase { position: absolute; left: 0; top: 663px; width: 996px; height: 537px; background: var(--teal); }

  .option-number {
    position: absolute; width: 50px; height: 50px; border: 2px solid var(--paper); border-radius: 50%;
    color: var(--paper); font-family: "EB Garamond", serif; font-weight: 600; font-size: 34px;
    display: flex; align-items: center; justify-content: center; line-height: 1;
  }
  .option-number--one { left: 239px; top: 94px; }
  .option-number--two { left: 708px; top: 94px; }

  .sticker { position: absolute; display: block; }
  .sticker--hero { left: 200px; top: 174px; width: 595px; height: 315px; filter: drop-shadow(0 6px 14px rgba(0,0,0,.12)); }
  .sticker--ticket { left: 78px; top: 214px; width: 372px; height: 197px; }
  .sticker--badge { left: 547px; top: 151px; width: 372px; height: 259px; }

  .headline { font-family: "EB Garamond", serif; font-weight: 700; fill: var(--ink); }
  .subline { font-family: "Noto Sans", sans-serif; font-weight: 700; fill: var(--ink); letter-spacing: .06em; }
  .contents { font-family: "Noto Sans", sans-serif; font-weight: 400; fill: var(--ink); }
  .contact { font-family: "Noto Sans", sans-serif; fill: var(--ink); }
  .contact--bold { font-weight: 700; }
  .brand-name { font-family: "EB Garamond", serif; font-weight: 700; fill: var(--ink); }
  .icon-line { fill: none; stroke: var(--ink); stroke-width: .9; }
</style>
</head>
<body>

<section class="stage">
  <svg class="sticker sticker--hero" viewBox="0 0 372 197" aria-label="Aufkleber Variante 1, flach">
    <defs>
      <linearGradient id="hero-leaf" x1="0" y1="0" x2="1" y2="1">
        <stop offset="0" stop-color="var(--leaf)"/>
        <stop offset=".45" stop-color="var(--paper)"/>
        <stop offset="1" stop-color="var(--leaf-soft)"/>
      </linearGradient>
      <clipPath id="hero-shape">
        <path d="M34,0 H338 A34,34 0 0 0 372,34 V163 A34,34 0 0 0 338,197 H34 A34,34 0 0 0 0,163 V34 A34,34 0 0 0 34,0 Z"/>
      </clipPath>
    </defs>
    <path d="M34,0 H338 A34,34 0 0 0 372,34 V163 A34,34 0 0 0 338,197 H34 A34,34 0 0 0 0,163 V34 A34,34 0 0 0 34,0 Z" fill="var(--paper)"/>
    <rect role="img" aria-label="Zarte Blätter- und Pflanzenmotive in Blaugrau als Hintergrund" x="0" y="0" width="372" height="197" fill="url(#hero-leaf)" clip-path="url(#hero-shape)" opacity=".9"/>
    <text class="headline" x="189" y="55" font-size="26" text-anchor="middle" textLength="225">GESTALTE DEIN</text>
    <text class="headline" x="189" y="85" font-size="26" text-anchor="middle" textLength="336">KUNSTWERK ZU HAUSE!</text>
    <circle cx="63" cy="127" r="23" fill="var(--badge)"/>
    <text class="brand-name" x="70" y="149" font-size="10" text-anchor="middle">PINSELHAUS</text>
    <text class="subline" x="134" y="110" font-size="9.6" textLength="222">DEIN KOMPLETTES KERAMIK-MALSET</text>
    <text class="contents" x="134" y="123" font-size="7.4">inkl. Rohling, Farben, Pinsel &amp; Zubehör.</text>
    <rect x="134" y="132" width="225" height="2" fill="var(--rule)"/>
    <g class="icon-line" transform="translate(139 146)">
      <circle r="4.3"/><ellipse rx="1.9" ry="4.3"/><line x1="-4.3" x2="4.3"/>
    </g>
    <text class="contact" x="146" y="149" font-size="8.8">www.pinselhaus.de</text>
    <text class="contact" x="134" y="162" font-size="8.8">Bilderwand/Freundesbuch: @pinselhaus</text>
  </svg>
</section>

<section class="showcase">
  <div class="option-number option-number--one">1</div>
  <div class="option-number option-number--two">2</div>

  <svg class="sticker sticker--ticket" viewBox="0 0 372 197" aria-label="Aufkleber Variante 1">
    <defs>
      <linearGradient id="ticket-leaf" x1="0" y1="0" x2="1" y2="1">
        <stop offset="0" stop-color="var(--leaf)"/>
        <stop offset=".45" stop-color="var(--paper)"/>
        <stop offset="1" stop-color="var(--leaf-soft)"/>
      </linearGradient>
      <clipPath id="ticket-shape">
        <path d="M34,0 H338 A34,34 0 0 0 372,34 V163 A34,34 0 0 0 338,197 H34 A34,34 0 0 0 0,163 V34 A34,34 0 0 0 34,0 Z"/>
      </clipPath>
    </defs>
    <path d="M34,0 H338 A34,34 0 0 0 372,34 V163 A34,34 0 0 0 338,197 H34 A34,34 0 0 0 0,163 V34 A34,34 0 0 0 34,0 Z" fill="var(--paper)"/>
    <rect role="img" aria-label="Zarte Blätter- und Pflanzenmotive in Blaugrau als Hintergrund" x="0" y="0" width="372" height="197" fill="url(#ticket-leaf)" clip-path="url(#ticket-shape)" opacity=".9"/>
    <text class="headline" x="189" y="55" font-size="26" text-anchor="middle" textLength="225">GESTALTE DEIN</text>
    <text class="headline" x="189" y="85" font-size="26" text-anchor="middle" textLength="336">KUNSTWERK ZU HAUSE!</text>
    <circle cx="63" cy="127" r="23" fill="var(--badge)"/>
    <text class="brand-name" x="70" y="149" font-size="10" text-anchor="middle">PINSELHAUS</text>
    <text class="subline" x="134" y="110" font-size="9.6" textLength="222">DEIN KOMPLETTES KERAMIK-MALSET</text>
    <text class="contents" x="134" y="123" font-size="7.4">inkl. Rohling, Farben, Pinsel &amp; Zubehör.</text>
    <rect x="134" y="132" width="225" height="2" fill="var(--rule)"/>
    <g class="icon-line" transform="translate(139 146)">
      <circle r="4.3"/><ellipse rx="1.9" ry="4.3"/><line x1="-4.3" x2="4.3"/>
    </g>
    <text class="contact" x="146" y="149" font-size="8.8">www.pinselhaus.de</text>
    <text class="contact" x="134" y="162" font-size="8.8">Bilderwand/Freundesbuch: @pinselhaus</text>
  </svg>

  <svg class="sticker sticker--badge" viewBox="0 0 372 259" aria-label="Aufkleber Variante 2">
    <g fill="var(--paper)">
      <rect x="0" y="66" width="372" height="193" rx="10"/>
      <circle cx="281" cy="50" r="50"/>
      <circle cx="244" cy="36" r="16"/>
      <circle cx="318" cy="36" r="16"/>
      <path d="M200,67 C218,64 226,52 236,44 L326,44 C336,52 344,64 362,67 Z"/>
    </g>
    <circle cx="284" cy="69" r="31" fill="var(--badge)"/>
    <text class="brand-name" x="290" y="91" font-size="12.5" text-anchor="middle">PINSELHAUS</text>
    <text class="headline" x="24" y="110" font-size="22" textLength="192">GESTALTE DEIN</text>
    <text class="headline" x="24" y="137" font-size="22" textLength="292">KUNSTWERK ZU HAUSE!</text>
    <rect x="21" y="148" width="340" height="4" rx="2" fill="var(--badge)"/>
    <text class="subline" x="23" y="175" font-size="13.2" textLength="337">DEIN KOMPLETTES KERAMIK-MALSET</text>
    <text class="contents" x="23" y="194" font-size="11.4">inkl. Rohling, Farben, Pinsel &amp; Zubehör.</text>
    <g class="icon-line" transform="translate(29 217)">
      <circle r="5.2"/><ellipse rx="2.3" ry="5.2"/><line x1="-5.2" x2="5.2"/>
    </g>
    <text class="contact contact--bold" x="41" y="221" font-size="10.5">www.pinselhaus.de</text>
    <text class="contact contact--bold" x="23" y="238" font-size="10.5">Bilderwand/Freundesbuch: @pinselhaus</text>
    <rect role="img" aria-label="Symbol einer Vase mit Pinsel" x="290" y="183" width="63" height="57" rx="8" fill="var(--leaf)"/>
  </svg>
</section>

</body>
</html>
```